sailbuddies Website for children with diabilities

Hi, we are looking for a new website design for our community service "sailbuddies". Sailbuddies gives children who suffer from diseases or disabilities a week off on a Boat to give the children new hope and an unforgettable experience.

The current website is really old and we want to have a new one.
Please feel free to discover our website under http://sailbuddies-example.at/.
We have several company sponsors which are very important to us.

The Website has to be a Bootstrap Design (Version 4.4 or higher) [NOT Wordpress, Joomla, other CMS]

Target Market(s)

no target market. we like to inform our communities about our service.

Industry/Entity Type

community service for children with disabilities

Coding

Coded - Design and coding required

Number of Pages Required

4 page

Font styles to use
Sans Serif

Colors
0054AA
0677BA
7BADD7
CADEEF
E8F1F8
0094D4
00A9DD
6FCCEA
C7EBF8
E9F6FB

Requirements
Must have
• About, Sponsors, Information about cruises
Nice to have
• Gallery

```html
<!DOCTYPE html>
<html lang="en">
<head>
<meta charset="utf-8">
<title>Sailbuddies – New Hope</title>
<link href="https://fonts.googleapis.com/css2?family=Poppins:wght@300;400;500;600;700&family=Kaushan+Script&family=PT+Serif&family=Kalam:wght@300&display=swap" rel="stylesheet">
<style>
:root{
  --navy:#0d1b4a;
  --navy-deep:#0a1538;
  --orange:#f7a21b;
  --blue:#0054AA;
  --blue-mid:#0677BA;
  --sky:#7BADD7;
  --ice:#E8F1F8;
  --ink:#1e1e24;
  --muted:#6d6f78;
  --card:#f7f8fb;
  --foot:#f5f6f9;
}
*{box-sizing:border-box;margin:0;padding:0}
html,body{width:1200px;height:3000px;overflow:hidden;background:#fff}
body{position:relative;font-family:"Poppins",sans-serif;color:var(--ink)}
.abs{position:absolute}
.btn{position:absolute;display:flex;align-items:center;justify-content:center;gap:6px;border-radius:20px;font:600 12px "Poppins",sans-serif;letter-spacing:1px;color:#fff;background:var(--orange)}
.btn.navy{background:var(--blue)}

/* hero */
.hero-bg{position:absolute;left:100px;top:0;width:1000px;height:500px}
.brand{position:absolute;left:149px;top:27px;width:88px;height:88px;border-radius:50%;border:4px solid #8e9bbd;background:var(--navy);display:flex;align-items:center;justify-content:center;color:#fff;font:600 11px "Poppins",sans-serif}
.nav{position:absolute;top:62px;left:343px;display:flex;gap:30px;font:500 12px "Poppins",sans-serif;letter-spacing:1px;color:#fff}
.phone{position:absolute;top:61px;left:728px;display:flex;align-items:center;gap:5px;font:500 12.5px "Poppins",sans-serif;letter-spacing:1px;color:#fff}
.hero-script{position:absolute;left:0;width:1200px;top:140px;text-align:center;font:58px "Kaushan Script",cursive;color:var(--orange)}
.hero-title{position:absolute;left:0;width:1200px;top:192px;text-align:center;font:300 44px/50px "Poppins",sans-serif;letter-spacing:4px;color:#fff}

/* intro */
.kicker{position:absolute;left:0;width:1200px;top:541px;text-align:center;font:11px "PT Serif",serif;letter-spacing:1.5px;color:var(--blue)}
.h2{position:absolute;left:0;width:1200px;text-align:center;font:600 29px "Poppins",sans-serif;color:var(--ink)}
.card{position:absolute;top:620px;width:164px;height:215px;background:var(--card);border-radius:14px;text-align:center;padding-top:26px}
.card .icon{width:64px;height:64px;margin:0 auto;border-radius:50%;background:#e3e6ee}
.card h3{font:600 14.5px "Poppins",sans-serif;letter-spacing:.5px;margin-top:14px}
.card .bar{width:26px;height:2px;background:var(--orange);margin:6px auto 10px}
.card p{font:300 10.5px/16px "Poppins",sans-serif;color:#333;padding:0 18px}

/* story */
.story-photo{position:absolute;left:232px;top:915px;width:414px;height:293px;border-radius:0 22px 0 22px;background:linear-gradient(135deg,#7fb5db,#3d7fb5 55%,#d2b690)}
.story-card{position:absolute;left:600px;top:952px;width:367px;height:260px;background:#fff;border-radius:8px;box-shadow:0 6px 24px rgba(20,30,60,.08);padding:60px 40px 0 30px}
.story-card .quote{font:13px/17px "PT Serif",serif;color:#444}
.story-card .sub{font:300 11px "Poppins",sans-serif;color:#999;margin-top:12px}
.quote-mark{position:absolute;right:48px;top:20px;font:120px/1 "PT Serif",serif;color:#eef0f4}

/* sponsors */
.lead{position:absolute;left:290px;width:620px;top:1318px;text-align:center;font:300 10.5px/18px "Poppins",sans-serif;color:#555}
.sponsor{position:absolute;top:1402px;font:700 17px "Poppins",sans-serif;color:#37435e;display:flex;align-items:center;gap:6px}
.sponsor i{display:block;width:12px;height:12px;background:var(--orange)}
.dot{position:absolute;top:1461px;width:6px;height:6px;border-radius:50%;background:#d5d8df}
.dot.on{background:var(--blue)}

/* gallery */
.tile{position:absolute;top:1540px;height:293px}

/* stats */
.stat{position:absolute;top:1990px;width:240px;text-align:center}
.stat b{display:block;font:300 56px/1 "Kalam",cursive;color:var(--orange)}
.stat p{font:300 10.5px/17px "Poppins",sans-serif;color:#555;margin-top:12px}
.divider{position:absolute;top:1990px;width:1px;height:148px;background:#e6e8ee}

/* about */
.about-card{position:absolute;left:520px;top:2190px;width:447px;height:336px;background:#fff;border-radius:8px;box-shadow:0 6px 24px rgba(20,30,60,.06)}
.about-text{position:absolute;left:632px;top:2243px;width:290px}
.about-text h2{font:600 26px "Poppins",sans-serif}
.about-text .serif{font:12.5px/17px "PT Serif",serif;color:#444;margin-top:14px}
.about-text .sans{font:300 10.5px/17px "Poppins",sans-serif;color:#555;margin-top:18px}

/* footer */
.footer{position:absolute;left:100px;top:2610px;width:1000px;height:306px;background:var(--foot)}
.footer-rule{position:absolute;left:232px;top:2610px;width:736px;height:1px;background:#e3e5eb}
.foot-brand{position:absolute;left:232px;top:2722px;width:76px;height:76px;border-radius:50%;background:var(--navy);border:3px solid #c5cbe0;display:flex;align-items:center;justify-content:center;color:#fff;font:600 9px "Poppins",sans-serif}
.fh{position:absolute;top:2680px;font:600 11px/15px "Poppins",sans-serif;color:var(--ink)}
.fcol{position:absolute;font:400 11px/19px "Poppins",sans-serif;color:#555}
.flink{position:absolute;left:615px;font:400 11px "Poppins",sans-serif;letter-spacing:1px;color:#666}
.email{position:absolute;left:756px;top:2750px;width:178px;height:34px;border:1px solid #dfe2e8;border-radius:17px;background:#fff;font:400 10px "Poppins",sans-serif;color:#555;padding:10px 16px}
.copy{position:absolute;left:100px;top:2916px;width:1000px;height:44px;background:var(--blue);color:#d7e4f4;font:300 10.5px/44px "Poppins",sans-serif;text-align:center}
</style>
</head>
<body>

<!-- hero -->
<svg class="hero-bg" viewBox="0 0 1000 500" role="img" aria-label="Photo of a mother and child sitting on stairs, dark blue tinted">
  <defs>
    <linearGradient id="heroFill" x1="0" y1="0" x2="1" y2="0">
      <stop offset="0" stop-color="#0d1b4a"/>
      <stop offset=".5" stop-color="#1c2a52"/>
      <stop offset="1" stop-color="#3a3f52"/>
    </linearGradient>
  </defs>
  <path d="M0 0H1000V420C900 400 820 440 720 480C640 510 560 505 470 470C330 410 170 362 0 361Z" fill="url(#heroFill)"/>
</svg>
<div class="brand">Sailbuddies</div>
<nav class="nav"><span>HOME</span><span>SPONSORS</span><span>ABOUT</span><span>GALLERY</span><span>BLOG</span></nav>
<div class="phone">
  <svg width="14" height="14" viewBox="0 0 24 24" fill="none" stroke="#fff" stroke-width="2"><path d="M5 3h4l2 5-3 2a12 12 0 0 0 6 6l2-3 5 2v4a2 2 0 0 1-2 2A18 18 0 0 1 3 5a2 2 0 0 1 2-2z"/></svg>
  +(43) 1200 450 780
</div>
<div class="btn" style="left:907px;top:54px;width:141px;height:34px">DONATE NOW →</div>
<div class="hero-script">New Hope</div>
<div class="hero-title">&amp; An Unforgettable<br>Experience.</div>
<div class="btn" style="left:530px;top:318px;width:141px;height:34px">DONATE NOW →</div>

<!-- intro -->
<div class="kicker">WHO WE ARE.</div>
<div class="h2" style="top:557px">Make a Difference</div>
<div class="card" style="left:232px"><div class="icon" role="img" aria-label="Line icon for social skills"></div><h3>Social Skills</h3><div class="bar"></div><p>Lorem ipsum dolor sit amet, consectetur adipi scing elit, sed do eiusmo...</p></div>
<div class="card" style="left:421px"><div class="icon" role="img" aria-label="Line icon of a monitor with charts"></div><h3>Nemo Tnim</h3><div class="bar"></div><p>Lorem ipsum dolor sit amet, consectetur adipi scing elit, sed do eiusmo...</p></div>
<div class="card" style="left:611px"><div class="icon" role="img" aria-label="Line icon of stacked books"></div><h3>Nisi ut Aliquid</h3><div class="bar"></div><p>Lorem ipsum dolor sit amet, consectetur adipi scing elit, sed do eiusmo...</p></div>
<div class="card" style="left:801px"><div class="icon" role="img" aria-label="Line icon of hearts and a stethoscope"></div><h3>Minim Beniam</h3><div class="bar"></div><p>Lorem ipsum dolor sit amet, consectetur adipi scing elit, sed do eiusmo...</p></div>

<!-- story -->
<div class="story-photo" role="img" aria-label="Photo of a child in a life jacket on a sailing boat"></div>
<div class="story-card">
  <div class="quote-mark">”</div>
  <p class="quote">Sed ut perspiciatis unde omnis iste natus error sit volup tatem accusantium doloremque laudantium, totam rem aperiam, eaque ipsa quae ab illo inventore</p>
  <p class="sub">Quis autem vel eum iure reprehe nderit qui</p>
  <div class="btn navy" style="left:32px;top:183px;width:142px;height:34px">DONATE NOW →</div>
</div>

<!-- sponsors -->
<div class="h2" style="top:1270px">Committed to Transparency</div>
<p class="lead">Lorem ipsum dolor sit amet, consectetur adipiscing elit, sed do eiusmod tempor incididunt ut labore et dolore magna aliqua. Ut enim ad minim veniam, quis nostrud exercitation ullamco laboris nisi ut aliquip ex ea commodo consequat.</p>
<div class="sponsor" style="left:232px">Bergwerk</div>
<div class="sponsor" style="left:402px"><i></i>Voltwerk</div>
<div class="sponsor" style="left:560px">Wellenreisen</div>
<div class="sponsor" style="left:728px">Hofmeister</div>
<div class="sponsor" style="left:884px"><i></i>Talbrunn</div>
<div class="dot" style="left:581px"></div><div class="dot on" style="left:596px"></div><div class="dot" style="left:611px"></div>

<!-- gallery -->
<div class="tile" style="left:100px;width:146px;background:linear-gradient(160deg,#5a4638,#c9a98a);border-radius:0 18px 0 0" role="img" aria-label="Photo of a father helping his daughter at a desk"></div>
<div class="tile" style="left:249px;width:232px;background:linear-gradient(160deg,#6aa350,#d8c9b0);border-radius:18px 0 18px 0" role="img" aria-label="Photo of two children eating fruit"></div>
<div class="tile" style="left:484px;width:231px;background:linear-gradient(160deg,#0a4e9e,#0054AA);border-radius:0 18px 0 18px" role="img" aria-label="Photo of a smiling child with blue overlay">
  <svg class="abs" style="left:108px;top:138px" width="16" height="16" viewBox="0 0 24 24" fill="none" stroke="#fff" stroke-width="2.5"><circle cx="10" cy="10" r="7"/><path d="M15 15l6 6"/></svg>
</div>
<div class="tile" style="left:718px;width:232px;background:linear-gradient(160deg,#8a5a46,#6d9fb0);border-radius:0 0 18px 18px" role="img" aria-label="Photo of a smiling boy in a wheelchair"></div>
<div class="tile" style="left:953px;width:147px;background:linear-gradient(160deg,#8f6a50,#3c3a38);border-radius:18px 0 0 0" role="img" aria-label="Photo of hands reaching for an orange"></div>

<!-- stats -->
<div class="h2" style="top:1895px">Quis Autem Beleum</div>
<div class="stat" style="left:219px"><b>125</b><p>Quis autem vel eum iure repr<br>ehe nderit qui in ea voluptate velit ess<br>equam nihil molesti...</p></div>
<div class="divider" style="left:470px"></div>
<div class="stat" style="left:480px"><b>1890</b><p>Quis autem vel eum iure repr<br>ehe nderit qui in ea voluptate velit ess<br>equam nihil molesti...</p></div>
<div class="divider" style="left:730px"></div>
<div class="stat" style="left:735px"><b>6.8M</b><p>Quis autem vel eum iure repr<br>ehe nderit qui in ea voluptate velit ess<br>equam nihil molesti...</p></div>

<!-- about -->
<div class="about-card"></div>
<svg class="abs" style="left:232px;top:2190px" width="357" height="336" viewBox="0 0 357 336" role="img" aria-label="Photo of a cruise ship at sunset">
  <defs><linearGradient id="sunset" x1="0" y1="0" x2="0" y2="1"><stop offset="0" stop-color="#f39a1e"/><stop offset=".5" stop-color="#e5612a"/><stop offset="1" stop-color="#8a2c22"/></linearGradient></defs>
  <path d="M0 0H357C340 60 300 70 290 140C280 210 320 250 290 300C270 330 230 336 200 336H22A22 22 0 0 1 0 314Z" fill="url(#sunset)"/>
</svg>
<div class="about-text">
  <h2>About Us</h2>
  <p class="serif">Sed ut perspiciatis unde omnis iste natus err orsit volup tatem accusantium doloremque lau dathtium, totam rem aperi.</p>
  <p class="sans">Sed ut perspiciatis unde omnis iste natus error si tvolup tatem accusantium doloremque loud antium, totam rem aperiam, eaque ipsa quae ab illo inventore veritatis et quas</p>
</div>
<div class="btn" style="left:632px;top:2440px;width:142px;height:34px">DONATE NOW →</div>

<!-- footer -->
<div class="footer"></div>
<div class="footer-rule"></div>
<div class="foot-brand">Sailbuddies</div>
<div class="fh" style="left:375px">Do you have questions?<br>Call or visit us.</div>
<div class="fcol" style="left:375px;top:2726px;color:var(--orange);font-weight:500">+(43) 1200 450 781</div>
<div class="fcol" style="left:375px;top:2755px;width:200px;line-height:14px">123, Lorem ipsum dolor sit amet, consec 567, Adipisc</div>
<div class="fcol" style="left:375px;top:2794px">contact@example.com</div>
<div class="fcol" style="left:375px;top:2825px;font-size:9px;color:#444;letter-spacing:1px">FB · TW · IG · YT · IN</div>
<div class="fh" style="left:615px">Quick Links</div>
<div class="flink" style="top:2724px">HOME</div>
<div class="flink" style="top:2750px">Sponsors</div>
<div class="flink" style="top:2776px">ABOUT</div>
<div class="flink" style="top:2802px">Gallery</div>
<div class="flink" style="top:2828px">BLOG</div>
<div class="fh" style="left:756px">Newsletter</div>
<div class="email">Your Email</div>
<div class="btn" style="left:758px;top:2774px;width:142px;height:34px">SUBSCRIBE</div>
<div class="copy">© Copyright 2022 Sailbuddies. All rights reserved.</div>

</body>
</html>
```